Business Card Design

we need a bussiness card for the transport company called Harvel Transport
name of contact person that should display on card is Mankirat Sekhon contact no 0478162093
we do the dry goods and frozen deliveries in melbourne every day
happy to beat any quote

Business

Contact Information for Business Card

Harvel transport
Mankirat sekhon
mob 0478162093
contact us for any refrigerator or dry goods delivery
deliver all over melbourne

```html
<!DOCTYPE html>
<html lang="en">
<head>
<meta charset="utf-8">
<title>Harvel Transport – Business Card</title>
<link href="https://fonts.googleapis.com/css2?family=Arimo:wght@400;700&family=Roboto:wght@300&display=swap" rel="stylesheet">
<style>
  :root {
    --brand-red: #9c2322;
    --brand-red-light: #b53a36;
    --card-grey: #ebebeb;
    --page-bg: #f6f6f6;
    --white: #ffffff;
  }
  * { margin: 0; padding: 0; box-sizing: border-box; }
  html, body {
    width: 946px;
    height: 1200px;
    overflow: hidden;
    background: var(--page-bg);
  }
  .business-card {
    position: absolute;
    left: 23px;
    top: 366px;
    width: 900px;
    height: 468px;
    background: var(--card-grey);
    overflow: hidden;
    box-shadow: 0 2px 10px rgba(0,0,0,0.12);
  }
  .card-shapes {
    position: absolute;
    inset: 0;
  }
  .brand {
    position: absolute;
    left: 14px;
    top: 240px;
    color: var(--white);
    font-family: "Roboto", sans-serif;
    font-weight: 300;
    line-height: 1;
  }
  .brand-name { font-size: 50px; letter-spacing: 0.5px; }
  .brand-sub { font-size: 34px; margin-top: 8px; padding-left: 4px; }
  .contact-name {
    position: absolute;
    left: 370px;
    top: 168px;
    font-family: "Arimo", sans-serif;
    font-weight: 700;
    font-size: 48px;
    color: var(--brand-red);
  }
  .contact-phone {
    position: absolute;
    right: 48px;
    top: 300px;
    display: flex;
    align-items: center;
    gap: 10px;
    font-family: "Arimo", sans-serif;
    font-weight: 700;
    font-size: 56px;
    line-height: 1;
    color: var(--brand-red);
  }
  .phone-icon { width: 40px; height: 40px; }
  .contact-cta {
    position: absolute;
    right: 72px;
    top: 362px;
    font-family: "Arimo", sans-serif;
    font-weight: 700;
    font-size: 40px;
    line-height: 1;
    color: var(--brand-red);
  }
  .service-band {
    position: absolute;
    left: 0;
    bottom: 0;
    width: 100%;
    height: 64px;
    background: var(--brand-red);
    color: var(--white);
    font-family: "Arimo", sans-serif;
    font-size: 24.5px;
    display: flex;
    align-items: center;
    justify-content: center;
    white-space: nowrap;
  }
</style>
</head>
<body>
  <section class="business-card">
    <svg class="card-shapes" width="900" height="468" viewBox="0 0 900 468" aria-hidden="true">
      <path d="M0 0 H300 C350 120 320 290 200 404 H0 Z" fill="var(--brand-red)"/>
      <path d="M316 0 C366 125 336 292 218 404" fill="none" stroke="var(--brand-red)" stroke-width="8"/>
      <circle cx="150" cy="118" r="62" fill="none" stroke="var(--white)" stroke-width="2"/>
    </svg>

    <div class="brand">
      <div class="brand-name">HARVEL</div>
      <div class="brand-sub">TRANSPORT</div>
    </div>

    <h1 class="contact-name">Mankirat Sekhon</h1>

    <div class="contact-phone">
      <svg class="phone-icon" viewBox="0 0 24 24" aria-hidden="true">
        <path fill="var(--brand-red)" d="M6.6 10.8a15.1 15.1 0 0 0 6.6 6.6l2.2-2.2a1 1 0 0 1 1-.25 11.4 11.4 0 0 0 3.6.57 1 1 0 0 1 1 1V20a1 1 0 0 1-1 1A17 17 0 0 1 3 4a1 1 0 0 1 1-1h3.5a1 1 0 0 1 1 1c0 1.25.2 2.45.57 3.57a1 1 0 0 1-.25 1z"/>
      </svg>
      <span>0478162093</span>
    </div>
    <div class="contact-cta">CONTACT US</div>

    <div class="service-band">For Any Refrigerator or Dry Goods Delivery Deliver all over Melbourne</div>
  </section>
</body>
</html>
```